Brightford Lingua Partners, LLC

We need a business card that includes information about our business and conveys a reliable business that provides document translation services and interpreters for a variety of corporate and individual clients. We want to come across as professional, reliable, yet approachable. It should include the following on one side:

ESL / ENL Language Classes, Private Lessons, and Online Tutors
PALQE Training and Testing
Translating & Interpreting Services
Contact us about Over-the-Phone Interpreting in over 200 languages
24/7/365
www.brightfordlingua.example

The other side should include (555) 481-3062

Marla Quennick, President
412 Garvin Ave., Ste. 209
Indianapolis, IN 46999
Updates

Please add USA as part of the address. Also, please add mrqquennick@brightfordlinguapartners.example as the e-mail address. Thank you.

Target Market(s)

Business professionals, their families, the international community

Industry/Entity Type

Business

Contact Information for Business Card

24/7/365
www.brightfordlingua.example

(555) 481-3062

Marla Quennick, President
412 Garvin Ave., Ste. 209
Indianapolis, IN 46999
USA

Font styles to use
Sans Serif

Colors

Designer to choose colors to be used in the design.

Requirements
Must have
• See project description
• e-mail address and web address
• Phone number
Nice to have
• a globe
• physical address
Should not have
• Should not have the same color scheme as other agencies in our market in Indiana unless it is blue and black. No purple or yellow.

```html
<!DOCTYPE html>
<html lang="en">
<head>
<meta charset="utf-8">
<title>Brightford Lingua Partners – Business Card</title>
<link href="https://fonts.googleapis.com/css2?family=Roboto:wght@400;500;700&display=swap" rel="stylesheet">
<style>
  :root {
    --ink: #111111;
    --brand-blue: #2596d6;
    --ribbon-grey: #bdbdbd;
    --ribbon-fold: #8f8f8f;
    --paper: #ffffff;
    --stage: #2b2b2b;
  }
  * { box-sizing: border-box; margin: 0; padding: 0; }
  html, body { width: 1200px; height: 900px; overflow: hidden; }
  body {
    background: var(--stage);
    font-family: "Roboto", Arial, sans-serif;
    position: relative;
  }
  .card {
    position: absolute;
    width: 540px;
    height: 310px;
    background: var(--paper);
    border-radius: 18px;
    overflow: hidden;
    box-shadow: 0 12px 30px rgba(0,0,0,.45);
  }
  .card--front { left: 40px; top: 295px; }
  .card--back  { left: 620px; top: 295px; }

  /* brand lockup */
  .brand {
    position: absolute;
    display: flex;
    align-items: center;
  }
  .brand__dot {
    border-radius: 50%;
    background: var(--brand-blue);
    flex: none;
  }
  .brand__name {
    font-weight: 500;
    color: var(--ink);
    line-height: 1.08;
  }
  .card--front .brand { left: 110px; top: 30px; gap: 20px; }
  .card--front .brand__dot { width: 84px; height: 84px; }
  .card--front .brand__name { font-size: 27px; }

  .services {
    position: absolute;
    left: 0; right: 0; top: 150px;
    list-style: none;
    text-align: center;
    font-size: 11.5px;
    line-height: 17px;
    color: var(--ink);
  }
  .front__hours {
    position: absolute;
    left: 0; right: 0; top: 232px;
    text-align: center;
    font-size: 13px;
    font-weight: 700;
    color: var(--brand-blue);
  }
  .front__web {
    position: absolute;
    left: 0; right: 0; bottom: 28px;
    text-align: center;
    font-size: 13px;
    color: var(--ink);
    letter-spacing: .2px;
  }

  /* back side */
  .back__bg { position: absolute; inset: 0; }
  .card--back .brand { left: 26px; top: 108px; gap: 12px; }
  .card--back .brand__dot { width: 56px; height: 56px; }
  .card--back .brand__name { font-size: 18px; }

  .ribbon {
    position: absolute;
    left: 212px; top: 30px;
    width: 300px; height: 52px;
    background: var(--ribbon-grey);
    padding: 8px 0 0 62px;
  }
  .ribbon__name { font-size: 17px; font-weight: 700; color: var(--ink); }
  .ribbon__title { font-size: 10.5px; color: var(--ink); padding-left: 34px; }

  .contacts {
    position: absolute;
    left: 26px; bottom: 28px;
    list-style: none;
  }
  .contacts li {
    display: flex; align-items: center;
    gap: 8px;
    font-size: 11.5px;
    color: var(--ink);
    height: 21px;
  }
  .contacts .icon {
    width: 16px; height: 16px;
    background: var(--brand-blue);
    display: flex; align-items: center; justify-content: center;
    flex: none;
  }
  .contacts .icon svg { width: 11px; height: 11px; }

  .address {
    position: absolute;
    left: 335px; top: 170px;
    width: 190px;
    text-align: center;
    color: var(--paper);
    font-size: 12.5px;
    line-height: 1.35;
  }
  .address svg { display: block; margin: 0 auto 6px; }
</style>
</head>
<body>

  <section class="card card--front" aria-label="Card front">
    <div class="brand">
      <span class="brand__dot"></span>
      <span class="brand__name">Brightford<br>Lingua Partners<br>LLC</span>
    </div>
    <ul class="services">
      <li>ESL / ENL Language Classes, Private Lessons, and Online Tutors</li>
      <li>PALQE Training and Testing</li>
      <li>Translating &amp; Interpreting Services</li>
      <li>Contact us about Over-the-Phone Interpreting in over 200 languages</li>
    </ul>
    <p class="front__hours">24/7/365</p>
    <p class="front__web">www.brightfordlingua.example</p>
  </section>

  <section class="card card--back" aria-label="Card back">
    <svg class="back__bg" width="540" height="310" viewBox="0 0 540 310" aria-hidden="true">
      <polygon points="245,0 540,0 540,310 325,310" fill="var(--brand-blue)"/>
      <polygon points="245,0 250,0 330,310 325,310" fill="rgba(0,0,0,.12)"/>
      <polygon points="212,82 246,82 232,96" fill="var(--ribbon-fold)"/>
    </svg>

    <div class="ribbon">
      <p class="ribbon__name">Marla Quennick</p>
      <p class="ribbon__title">President</p>
    </div>

    <div class="brand">
      <span class="brand__dot"></span>
      <span class="brand__name">Brightford<br>Lingua Partners<br>LLC</span>
    </div>

    <ul class="contacts">
      <li><span class="icon"><svg viewBox="0 0 24 24"><path fill="#fff" d="M6.6 10.8a15 15 0 0 0 6.6 6.6l2.2-2.2c.3-.3.7-.4 1-.2 1.1.4 2.3.6 3.6.6.6 0 1 .4 1 1V20c0 .6-.4 1-1 1A17 17 0 0 1 3 4c0-.6.4-1 1-1h3.5c.6 0 1 .4 1 1 0 1.3.2 2.5.6 3.6.1.3 0 .7-.2 1z"/></svg></span>(555) 481-3062</li>
      <li><span class="icon"><svg viewBox="0 0 24 24"><rect x="4" y="9" width="16" height="11" rx="2" fill="#fff"/><path d="M3 8c3-4 15-4 18 0" stroke="#fff" stroke-width="2.5" fill="none"/></svg></span>(555) 207-4418</li>
      <li><span class="icon"><svg viewBox="0 0 24 24"><rect x="3" y="6" width="18" height="12" fill="none" stroke="#fff" stroke-width="2"/><path d="M3 6l9 7 9-7" fill="none" stroke="#fff" stroke-width="2"/></svg></span>mrqquennick@brightfordlinguapartners.example</li>
      <li><span class="icon"><svg viewBox="0 0 24 24"><circle cx="12" cy="12" r="9" fill="none" stroke="#fff" stroke-width="2"/><path d="M3 12h18M12 3c3 3 3 15 0 18M12 3c-3 3-3 15 0 18" fill="none" stroke="#fff" stroke-width="1.6"/></svg></span>www.brightfordlingua.example</li>
    </ul>

    <div class="address">
      <svg width="12" height="16" viewBox="0 0 12 16" aria-hidden="true"><path d="M6 0a6 6 0 0 1 6 6c0 4-6 10-6 10S0 10 0 6a6 6 0 0 1 6-6z" fill="#fff"/><circle cx="6" cy="6" r="2.2" fill="var(--brand-blue)"/></svg>
      412 Garvin Ave., Ste. 209<br>
      Indianapolis, IN 46999<br>
      USA
    </div>
  </section>

</body>
</html>
```